Transit Van Vehicle Wrap for Fenwick Meadow Gardens

We need to wrap two of our transit vans. One is a replacement. The old wrap had a back patio scene with patio furniture and lanscaping. Im not sure this is what we want moving forward. I want people to easily identify it is Fenwick Meadow Gardens when they look at the vehicle. Most recently we have wrapped our landscape trailers black, however with the base color being white and not wanting to wrap all of the vehicle, Im not sure black background is the way to go. We've also considered using 3 or 4 picture windows and a subtitle to describe what we do. We can to list words like Container Gardening, Backyard Patios, Houseplants, Plant Doctors, etc. instead of using department names to tell people what we do. We would like to use more specific words and words that formulate an image in your mind when you say it. Needs to have our logo in it. Sides and Rear doors. Rear should be logo with words or services listed. The sides could be the same or images. Ive attached two logos, one meant to be used overtop of darker background. We are a retail lifestyle garden center and landscape design build company, selling annuals, perennial, trees shrubs, lawn care items, gardening tools, house plants, pottery, patio furniture, mens and womens apparel and accessories, christmas decor and trees, lorne candles and other home fragrence, seasonal home decor and more. Visit fenwickmeadowgardens.com to see it all.

Target Market(s)

Home Owners in their 40s to 50s

Industry/Entity Type

lifestyle garden center and landscape firm

Requirements
Must have
• company logo and words describing what we do.

```html
<!DOCTYPE html>
<html lang="en">
<head>
<meta charset="utf-8">
<title>Fenwick Meadow Gardens – Van Side Wrap</title>
<link rel="stylesheet" href="https://fonts.googleapis.com/css2?family=Open+Sans:wght@500;700&display=swap">
<style>
  :root {
    --page-bg: #eceeea;
    --panel-bg: #ffffff;
    --service-band: #3aa6d9;
    --service-text: #ffffff;
    --brand-green: #5f8a2e;
    --brand-gold: #f1c232;
    --photo-deep: #4a3b2a;
    --photo-mid: #7d6a4e;
    --photo-leaf: #6f9a3c;
  }
  * { margin: 0; padding: 0; box-sizing: border-box; }
  html, body {
    width: 1200px;
    height: 1200px;
    overflow: hidden;
    background: var(--page-bg);
    font-family: "Open Sans", Arial, sans-serif;
  }
  .wrap-panel {
    position: absolute;
    left: 40px;
    top: 321px;
    width: 1120px;
    height: 557px;
    background: var(--panel-bg);
    overflow: hidden;
    box-shadow: 0 2px 10px rgba(0,0,0,0.12);
  }
  .brand-lockup {
    position: absolute;
    left: 60px;
    top: 120px;
    width: 480px;
    display: flex;
    align-items: center;
    justify-content: center;
    gap: 16px;
  }
  .brand-dot {
    width: 34px;
    height: 34px;
    border-radius: 50%;
    background: var(--brand-gold);
    flex: none;
  }
  .brand-name {
    font-weight: 700;
    font-size: 34px;
    color: var(--brand-green);
    white-space: nowrap;
    letter-spacing: 0.5px;
  }
  .service-band {
    position: absolute;
    left: 0;
    top: 324px;
    width: 533px;
    height: 172px;
    background: var(--service-band);
    padding: 22px 0 0 99px;
  }
  .service-list {
    list-style: none;
    color: var(--service-text);
    font-weight: 500;
    font-size: 26px;
    line-height: 35px;
    letter-spacing: 0.6px;
    text-transform: uppercase;
  }
  .photo-window {
    position: absolute;
    inset: 0;
    width: 1120px;
    height: 557px;
  }
</style>
</head>
<body>
  <section class="wrap-panel">
    <svg class="photo-window" viewBox="0 0 1120 557" aria-hidden="false">
      <defs>
        <radialGradient id="seedling-tones" cx="0.45" cy="0.4" r="0.7">
          <stop offset="0" stop-color="var(--photo-leaf)"/>
          <stop offset="0.45" stop-color="var(--photo-mid)"/>
          <stop offset="1" stop-color="var(--photo-deep)"/>
        </radialGradient>
      </defs>
      <circle cx="948" cy="468" r="414" fill="none" stroke="var(--brand-gold)" stroke-width="9"/>
      <circle cx="935" cy="472" r="402" fill="url(#seedling-tones)" role="img" aria-label="Photo of young seedlings sprouting in biodegradable peat pots"/>
    </svg>

    <div class="brand-lockup">
      <span class="brand-dot"></span>
      <span class="brand-name">Fenwick Meadow Gardens</span>
    </div>

    <div class="service-band">
      <ul class="service-list">
        <li>Container Gardening</li>
        <li>Backyard Patios</li>
        <li>Houseplants</li>
        <li>Plant Doctors, etc.</li>
      </ul>
    </div>
  </section>
</body>
</html>
```